Brochure to advertise our unique physiotherapy clinic to general practitioners

We want to advertise our unique physiotherapy clinic to general practitioners (GPs) to develop there awareness of both our existence and services offered. The brochure should highlight our uniqueness (i.e. providing the highest quality care, advice and education) based on our expert research-based knowledge and skills. After reading the brochure, we want GPs to feel like they know us a little and feel happy to refer their patients to our clinic.
Attached is a draft flyer containing our logo, contact details, profile pictures and the information we would like to be contained in the brochure. We would like the brochure to be A4 double sided and able to be folded to fit into an envelope. More material (pictures) and understanding of our clinic can be found at www.kinetreva.com.au

A brief background of our team:
Our team currently consists of two physiotherapists specialising in the management of musculoskeletal and sports injuries, Dr Howard Tenniscombe and Dr Lionel Fairweather. Both Howard and Lionel have completed PhDs related to musculosketal injury management, and continue to be actively involved in international research groups. Between them they have authored more than 50 peer reviewed papers, presented at countless national and international conferences, and coordinate numerous courses to facilitate professional development of other clinicians. Most importantly, they continue to enjoy mixing these research and teaching activities with treating patients.

Updates
Project Deadline Extended
Reason: Consultation with clinic partner is needed and to allow time for modifications and additional designs. We will pick one, just want quality.
Thanks

Project Deadline Extended

Thank you for some great designs thus far everyone. We have decided to remove the fees from the brochure so please do the same for any future submissions. In the process of trying to provide feedback now.
Thanks
Project Deadline Extended
Reason: A couple of designs are close and we want to allow time to make appropriate modifications. This will be the last extension. Thanks for everyones effort so far

Project Deadline Extended

Target Market(s)
Australian General Practitioners and other health professionals are the targeted audience
Industry/Entity Type
Clinic
Look and feel

```html
<!DOCTYPE html>
<html lang="en">
<head>
<meta charset="utf-8">
<title>Kinetreva – Clinic Brochure</title>
<link href="https://fonts.googleapis.com/css2?family=Arimo:wght@400;700&family=Tinos:ital@1&display=swap" rel="stylesheet">
<style>
  :root {
    --brand-blue: #1ba0d8;
    --panel-green: #b9dc8f;
    --panel-blue: #8fc3e8;
    --ink: #111111;
    --muted: #8a8a8a;
    --logo-grey: #6d6e71;
    --fold-line: #c8c8c8;
    --photo-warm: #8d8a84;
    --photo-green: #6d7f4c;
  }
  * { margin: 0; padding: 0; box-sizing: border-box; }
  html, body { width: 1200px; height: 848px; overflow: hidden; background: #fff; }
  body { font-family: "Arimo", Arial, sans-serif; color: var(--ink); }

  .brochure { position: relative; width: 1200px; height: 848px; overflow: hidden; background: #fff; }

  .panel { position: absolute; top: 0; height: 848px; }
  .panel--green {
    left: 0; width: 410px;
    background: radial-gradient(ellipse 230px 470px at 410px 424px, #fff 30%, rgba(255,255,255,0) 100%),
                linear-gradient(90deg, var(--panel-green), #eef6e2);
  }
  .panel--blue {
    left: 410px; width: 410px;
    background: radial-gradient(ellipse 260px 470px at 150px 424px, #fff 35%, rgba(255,255,255,0) 100%),
                linear-gradient(90deg, #eaf3fb, var(--panel-blue));
  }
  .panel--cover { left: 820px; width: 380px; background: #fff; border-left: 1px solid var(--fold-line); }

  .section-title {
    position: absolute; left: 0; height: 30px;
    background: var(--brand-blue); color: #fff;
    font-weight: 700; font-size: 20px; line-height: 30px; padding-left: 58px;
  }
  .section-title--clinic { top: 26px; width: 197px; }
  .section-title--team { top: 177px; width: 200px; }
  .section-title--services { top: 640px; width: 240px; }

  .copy {
    position: absolute; left: 60px; width: 718px;
    font-size: 11.4px; line-height: 15.5px; letter-spacing: -0.15px;
  }
  .copy--clinic { top: 82px; }
  .copy--team { top: 238px; }
  .copy--services { top: 706px; }
  .drop {
    font-family: "Tinos", "Times New Roman", serif; font-style: italic;
    font-size: 30px; line-height: 0; letter-spacing: 0;
  }
  .web-link { display: block; margin-top: 12px; color: var(--muted); font-weight: 700; }

  .portrait { position: absolute; }
  .portrait__shadow { position: absolute; background: #000; }
  .portrait__photo { position: absolute; }
  .portrait--howard .portrait__shadow { left: 181px; top: 326px; width: 219px; height: 241px; }
  .portrait--howard .portrait__photo {
    left: 197px; top: 333px; width: 213px; height: 242px;
    background: linear-gradient(160deg, #c9c6c0, var(--photo-warm) 60%, #2d3444);
  }
  .portrait--lionel .portrait__shadow { left: 410px; top: 377px; width: 218px; height: 233px; }
  .portrait--lionel .portrait__photo {
    left: 400px; top: 368px; width: 212px; height: 244px;
    background: linear-gradient(180deg, var(--photo-green), #b9a48d 55%, #f2f2f0 80%);
  }
  .caption { position: absolute; font-size: 11.4px; }
  .caption--howard { left: 197px; top: 581px; }
  .caption--lionel { left: 513px; top: 349px; }

  .brand { position: absolute; left: 836px; top: 300px; display: flex; align-items: center; gap: 14px; }
  .brand__mark { width: 48px; height: 48px; border-radius: 50%; background: var(--brand-blue); }
  .brand__name { font-size: 44px; font-weight: 700; color: var(--logo-grey); letter-spacing: -0.5px; }

  .contact { position: absolute; left: 835px; top: 714px; font-size: 11.4px; line-height: 15.5px; font-style: normal; }
  .contact p { margin: 0; }
</style>
</head>
<body>
<main class="brochure">
  <div class="panel panel--green"></div>
  <div class="panel panel--blue"></div>
  <div class="panel panel--cover"></div>

  <h2 class="section-title section-title--clinic">The Clinic</h2>
  <p class="copy copy--clinic"><span class="drop">W</span>e are a very unique and progressive physiotherapy clinic at Kinetreva. Our clinic is located within Solace Fitness, Level 4, 21-23, Marlow Avenue, Ashgrove East, VIC, 3127. Further information about us is detailed below. Additionally, please visit our website and join the associated ‘tendinopathy’ ‘patellofemoral’ and ‘biomechanics’ blogs if you are interested at:<span class="web-link">http://www.kinetreva.com.au/</span></p>

  <h2 class="section-title section-title--team">Who are we?</h2>
  <p class="copy copy--team"><span class="drop">O</span>ur team currently consists of two physiotherapists specialising in the management of musculoskeletal and sports injuries, Dr Howard Tenniscombe and Dr Lionel Fairweather. Both Howard and Lionel have completed PhDs related to musculoskeletal injury management, and continue to be actively involved in international research groups. Between them they have authored more than 40 peer reviewed papers, presented at countless national and international conferences, and coordinate numerous courses to facilitate professional development of other clinicians. Most importantly, they continue to enjoy mixing these research and teaching activities with treating patients.</p>

  <figure class="portrait portrait--howard">
    <div class="portrait__shadow"></div>
    <div class="portrait__photo" role="img" aria-label="Portrait photo of Dr Howard Tenniscombe"></div>
  </figure>
  <figure class="portrait portrait--lionel">
    <div class="portrait__shadow"></div>
    <div class="portrait__photo" role="img" aria-label="Portrait photo of Dr Lionel Fairweather"></div>
  </figure>
  <span class="caption caption--howard">Dr Howard Tenniscombe</span>
  <span class="caption caption--lionel">Dr Lionel Fairweather</span>

  <h2 class="section-title section-title--services">Services offered</h2>
  <p class="copy copy--services"><span class="drop">A</span>ll patients receive the highest quality 1-1 physiotherapy treatment and we offer patients accurate, realistic and lasting solution to their problems. We can guarantee the quality of our treatment because we are genuine experts in managing difficult injuries, with a wealth of clinical and research experience. This ultimately means we can more effective care, saving patients both time and money.</p>

  <div class="brand">
    <span class="brand__mark"></span>
    <span class="brand__name">Kinetreva</span>
  </div>

  <address class="contact">
    <p>c/o Solace Fitness, Level 4, The Atrium</p>
    <p>21-23 Marlow Ave, Ashgrove, 3128</p>
    <p>e: info@kinetreva.com.au</p>
    <p>w: www.kinetreva.com.au</p>
    <p>p: 9555 0148</p>
  </address>
</main>
</body>
</html>
```